Business card design for a teacher - double sided, sleek design.

My name is Dalia and I am an online Arabic language teacher. I am looking for a beautiful business card design for my online teaching business.

The cards will be printed in 85mm x 55mm size.
The card can be either portrait or landscape.

The design should contain my logo on one side and information on the other.

The design needs to be clean and modern. Use of subtle Arabic geometric patterns would be nice. Icons for the social media information on the card should also match the design theme.

My logo font is Consolas, which is a Monospace font.

Business card design should be delivered with editable PSD or EPS files in the handover.

Thanks

Dalia

----

Information on the back:

URL: www.lughapathway.net [this should stand out more than other details]
Email: info@lughapathway.net
Instagram: @lughapathway
Facebook: lughapathway.net/community
Skype: lughapathway

My brand colours are shown in the logo attached. These are:
- Teal green - 4DC9C1
- Mango yellow - FFD600

Target Market(s)

- Young professionals
- Expatriates
- Women and Men

Industry/Entity Type

Education

Contact Information for Business Card

Information on the back:

Skype: lughapathway

- Teal green - 4DC9C1
- Mango yellow - FFD600

Font styles to use
Other font styles liked:
• Any font complimentary to my logo font which is a Monospace font called Consolas.

Colors

Designer to choose colors to be used in the design.

Requirements
Must have
• - Aesthetically pleasing look
• - Complimentary design with existing logo
Nice to have
• Arabic geometrical patterns

```html
<!DOCTYPE html>
<html lang="en">
<head>
<meta charset="utf-8">
<title>Lugha Pathway – Business Card</title>
<link rel="stylesheet" href="https://fonts.googleapis.com/css2?family=Inconsolata:wght@500&family=Work+Sans:wght@400;700&display=swap">
<style>
  :root {
    --page-bg: #e6e1da;
    --card-dark: #3a3938;
    --teal: #4dc9a8;
    --teal-soft: #46b59c;
    --mango: #e8bf0e;
    --text-light: #cfcdc9;
    --icon-gold: #c9a514;
  }
  * { margin: 0; padding: 0; box-sizing: border-box; }
  html, body {
    width: 1200px;
    height: 1047px;
    overflow: hidden;
    background: var(--page-bg);
  }
  .card {
    position: absolute;
    left: 80px;
    top: 233px;
    width: 1040px;
    height: 580px;
    border-radius: 24px;
    overflow: hidden;
    background: var(--card-dark);
    box-shadow: 0 18px 40px rgba(0,0,0,0.18);
  }
  .card-header-art {
    position: absolute;
    left: 0;
    top: 0;
    width: 1040px;
    height: 118px;
    background: linear-gradient(180deg, var(--teal-soft) 0%, var(--teal) 70%, var(--mango) 100%);
  }
  .brand {
    position: absolute;
    left: 70px;
    top: 150px;
    display: flex;
    align-items: center;
    gap: 28px;
  }
  .brand-square {
    width: 130px;
    height: 134px;
    border: 3px solid var(--mango);
  }
  .brand-name {
    font-family: "Inconsolata", monospace;
    font-weight: 500;
    font-size: 50px;
    line-height: 1.15;
    letter-spacing: 6px;
    color: var(--text-light);
    text-transform: uppercase;
  }
  .divider {
    position: absolute;
    left: 55px;
    top: 347px;
    width: 745px;
    height: 2px;
    background: var(--teal);
  }
  .owner-name {
    position: absolute;
    right: 50px;
    top: 318px;
    font-family: "Work Sans", sans-serif;
    font-weight: 700;
    font-size: 50px;
    letter-spacing: 1px;
    color: var(--mango);
    text-transform: uppercase;
  }
  .contact-list {
    position: absolute;
    left: 58px;
    top: 384px;
    list-style: none;
  }
  .contact-item {
    display: flex;
    align-items: center;
    height: 33px;
    font-family: "Work Sans", sans-serif;
    font-weight: 400;
    font-size: 24px;
    color: var(--text-light);
  }
  .contact-icon {
    width: 18px;
    height: 18px;
    margin-right: 18px;
    flex: none;
  }
</style>
</head>
<body>
  <div class="card">
    <div class="card-header-art" role="img" aria-label="Decorative teal and mango wave band across the top of the card"></div>

    <div class="brand">
      <div class="brand-square"></div>
      <div class="brand-name">Lugha<br>Pathway</div>
    </div>

    <div class="divider"></div>
    <div class="owner-name">Dalia</div>

    <ul class="contact-list">
      <li class="contact-item">
        <svg class="contact-icon" viewBox="0 0 18 18" aria-hidden="true"><rect x="2" y="2" width="14" height="14" rx="2" fill="var(--icon-gold)"/></svg>
        @lughapathway
      </li>
      <li class="contact-item">
        <svg class="contact-icon" viewBox="0 0 18 18" aria-hidden="true"><circle cx="9" cy="9" r="7" fill="var(--icon-gold)"/></svg>
        lughapathway.net/community
      </li>
      <li class="contact-item">
        <svg class="contact-icon" viewBox="0 0 18 18" aria-hidden="true"><circle cx="9" cy="9" r="7" fill="none" stroke="var(--icon-gold)" stroke-width="2"/></svg>
        lughapathway
      </li>
      <li class="contact-item">
        <svg class="contact-icon" viewBox="0 0 18 18" aria-hidden="true"><rect x="2" y="4" width="14" height="10" fill="none" stroke="var(--icon-gold)" stroke-width="1.8"/><path d="M2,4 L9,10 L16,4" fill="none" stroke="var(--icon-gold)" stroke-width="1.8"/></svg>
        info@lughapathway.net
      </li>
      <li class="contact-item">
        <svg class="contact-icon" viewBox="0 0 18 18" aria-hidden="true"><circle cx="9" cy="9" r="7" fill="none" stroke="var(--icon-gold)" stroke-width="1.8"/><ellipse cx="9" cy="9" rx="3" ry="7" fill="none" stroke="var(--icon-gold)" stroke-width="1.4"/><path d="M2,9 H16" stroke="var(--icon-gold)" stroke-width="1.4"/></svg>
        www.lughapathway.net
      </li>
    </ul>
  </div>
</body>
</html>
```